Natural Organic soap need packaging design

we need a packaging design for new company based in New Zealand Called 'Tellum Global ltd'.. We manufacture Natural organic soap bars.our main USP is that this soap is made of all natural ingredient and no chemical used and soap is made in New Zealand,so we need a design which look natural,simple,classy and luxury and packaging should reflect that its made in New Zealand.please find attached photos of sample soap.
soap will be in two variant:
1. Pure Manuka Honey soap
2. Goat Milk soap
NOTE: the soap in picture is not actually our soap its just a sample what our soap will look like so please don't make a design with FRAKKK written on it. TELLUM is the soap name.
Target Market(s)
international market. mainly young and kids
Industry/Entity Type
It Company
Look and feel

```html
<!DOCTYPE html>
<html lang="en">
<head>
<meta charset="utf-8">
<title>Tellum New Zealand – Soap Packaging</title>
<link href="https://fonts.googleapis.com/css2?family=Bebas+Neue&family=Raleway:wght@400;500;700&display=swap" rel="stylesheet">
<style>
  :root {
    --ink: #231f20;
    --kraft: #c49a6c;
    --paper: #ffffff;
    --rule: #2a2320;
  }
  html, body {
    margin: 0;
    padding: 0;
    width: 1200px;
    height: 1167px;
    overflow: hidden;
    background: var(--paper);
  }
  .canvas {
    position: relative;
    width: 1200px;
    height: 1167px;
  }
  .pack {
    position: absolute;
    top: 245px;
    height: 572px;
    background: var(--kraft);
    color: var(--ink);
    font-family: "Raleway", sans-serif;
  }
  .pack--goat { left: 103px; width: 489px; }
  .pack--honey { left: 641px; width: 463px; }

  .pack__brand {
    position: absolute;
    left: 0; top: 0; right: 0;
    height: 255px;
    background: var(--ink);
    color: var(--paper);
    text-align: center;
  }
  .brand-name {
    position: absolute;
    left: 0; right: 0; top: 56px;
    font-family: "Raleway", sans-serif;
    font-weight: 700;
    font-size: 78px;
    line-height: 1;
    letter-spacing: 0.02em;
  }
  .brand-origin {
    position: absolute;
    left: 0; right: 0; top: 166px;
    font-family: "Raleway", sans-serif;
    font-weight: 700;
    font-size: 18px;
    letter-spacing: 0.5em;
    padding-left: 0.5em;
  }

  .rule-h, .rule-v {
    position: absolute;
    background: var(--rule);
  }
  .rule-h { height: 2px; }
  .rule-v { width: 2px; }

  .product-name {
    position: absolute;
    left: 0;
    top: 255px;
    height: 93px;
    display: flex;
    align-items: center;
    justify-content: center;
    text-align: center;
    font-family: "Bebas Neue", sans-serif;
    font-size: 32px;
    line-height: 1.05;
    letter-spacing: 0.01em;
  }
  .weight {
    position: absolute;
    top: 348px;
    height: 82px;
    display: flex;
    align-items: center;
    justify-content: center;
    font-family: "Bebas Neue", sans-serif;
    font-size: 30px;
  }
  .claim {
    position: absolute;
    top: 348px;
    height: 82px;
    display: flex;
    align-items: center;
    padding-left: 14px;
    font-size: 20px;
  }
  .product-art {
    position: absolute;
    top: 255px;
    height: 175px;
    display: flex;
    align-items: center;
    justify-content: center;
  }
  .art-fill {
    width: 160px;
    height: 124px;
    border-radius: 10px;
    background: radial-gradient(circle at 50% 50%, #2a2320 0%, #3b302a 55%, rgba(59,48,42,0) 80%);
  }
  .description {
    position: absolute;
    left: 24px; right: 24px;
    top: 443px;
    text-align: center;
    font-size: 16.5px;
    line-height: 1.4;
  }
  .social {
    position: absolute;
    left: 28px;
    top: 528px;
    display: flex;
    gap: 14px;
  }
  .social span {
    width: 26px;
    height: 26px;
    border-radius: 5px;
    background: var(--ink);
  }
  .imprint {
    position: absolute;
    right: 34px;
    top: 521px;
    text-align: right;
    line-height: 1.35;
  }
  .imprint .web { font-size: 11px; }
  .imprint .company { font-size: 13px; font-weight: 500; letter-spacing: 0.02em; }

  .signoff {
    position: absolute;
    left: 805px;
    top: 955px;
    width: 300px;
    text-align: center;
    color: var(--ink);
  }
  .signoff .brand-name {
    position: static;
    font-size: 64px;
  }
  .signoff .brand-origin {
    position: static;
    margin-top: 20px;
    font-size: 16px;
  }
</style>
</head>
<body>
<main class="canvas">

  <!-- Goat milk variant -->
  <section class="pack pack--goat">
    <header class="pack__brand">
      <div class="brand-name">TELLUM</div>
      <div class="brand-origin">NEW ZEALAND</div>
    </header>

    <div class="product-name" style="width:266px;">GOAT MILK SOAP</div>
    <div class="product-art" style="left:266px; right:0;">
      <div class="art-fill" role="img" aria-label="Dark silhouette illustration of a standing goat"></div>
    </div>
    <div class="weight" style="left:0; width:86px;">80G</div>
    <div class="claim" style="left:86px;">Natural organic</div>

    <div class="rule-h" style="left:0; right:0; top:254px;"></div>
    <div class="rule-h" style="left:0; width:266px; top:347px;"></div>
    <div class="rule-h" style="left:0; right:0; top:429px;"></div>
    <div class="rule-v" style="left:265px; top:255px; height:175px;"></div>
    <div class="rule-v" style="left:85px; top:348px; height:82px;"></div>

    <p class="description" style="margin:0;">This soap is made of all natural ingredient and no chemical used and soap is made in New Zealand.</p>

    <div class="social" aria-label="Social links"><span></span><span></span><span></span></div>
    <div class="imprint">
      <div class="web">www.tellum.co.nz</div>
      <div class="company">TELLUM GLOBAL LTD</div>
    </div>
  </section>

  <!-- Manuka honey variant -->
  <section class="pack pack--honey">
    <header class="pack__brand">
      <div class="brand-name">TELLUM</div>
      <div class="brand-origin">NEW ZEALAND</div>
    </header>

    <div class="product-name" style="width:272px;">PURE MANUKA HONEY<br>SOAP</div>
    <div class="product-art" style="left:272px; right:0;">
      <div class="art-fill" role="img" aria-label="Dark illustration of honeycomb cells with a honey bee"></div>
    </div>
    <div class="weight" style="left:0; width:93px;">80G</div>
    <div class="claim" style="left:93px;">Natural organic</div>

    <div class="rule-h" style="left:0; right:0; top:254px;"></div>
    <div class="rule-h" style="left:0; width:272px; top:347px;"></div>
    <div class="rule-h" style="left:0; right:0; top:429px;"></div>
    <div class="rule-v" style="left:271px; top:255px; height:175px;"></div>
    <div class="rule-v" style="left:92px; top:348px; height:82px;"></div>

    <p class="description" style="margin:0;">This soap is made of all natural ingredient and no chemical used and soap is made in New Zealand.</p>

    <div class="social" aria-label="Social links"><span></span><span></span><span></span></div>
    <div class="imprint">
      <div class="web">www.tellum.co.nz</div>
      <div class="company">TELLUM GLOBAL LTD</div>
    </div>
  </section>

  <!-- Brand sign-off -->
  <div class="signoff">
    <div class="brand-name">TELLUM</div>
    <div class="brand-origin">NEW ZEALAND</div>
  </div>

</main>
</body>
</html>
```